Web page design for podiatry office*

Need a web page for our podiatry office. It should feature most of our services, hours, directions and location. Should include a short bio of the doctor and a contact page.

Coding

Coded - Design and coding required

Number of Pages Required

1 page

Colors

Designer to choose colors to be used in the design.

```html
<!DOCTYPE html>
<html lang="en">
<head>
<meta charset="utf-8">
<title>Hollis Podiatry</title>
<link href="https://fonts.googleapis.com/css2?family=Montserrat:wght@400;500;600;700&display=swap" rel="stylesheet">
<style>
:root{
  --teal:#20c5b5;
  --teal-light:#55e6d8;
  --ink:#444444;
  --ink-dark:#222222;
  --band:#4d4d4d;
  --soft:#f7f7f7;
  --white:#ffffff;
  --red:#e0102a;
  --skin:#e9b59a;
}
*{box-sizing:border-box;margin:0;padding:0}
html,body{width:1200px;height:2508px;overflow:hidden}
body{position:relative;font-family:'Montserrat',sans-serif;color:var(--ink);background:var(--white)}
.abs{position:absolute}
a{color:inherit;text-decoration:none}

.brand{left:0;width:1200px;display:flex;justify-content:center;align-items:center;gap:12px}
.brand-dot{width:18px;height:18px;border-radius:50%;background:var(--teal)}
.brand-name{font-size:36px;font-weight:500;color:var(--ink)}
.site-header .brand{top:42px}

.main-nav{top:133px;left:0;width:1200px;height:51px;background:var(--teal)}
.main-nav a{position:absolute;top:0;height:51px;line-height:51px;font-size:15px;font-weight:600;color:#2b2b2b}
.main-nav a.active{background:var(--white);padding:0 17px}

.hero{top:184px;left:0;width:1200px;height:516px;background:linear-gradient(90deg,#fdfdfd 0%,#f6f6f6 100%)}
.hero-photo{top:0;left:480px;width:720px;height:516px;background:linear-gradient(90deg,rgba(250,250,250,1) 0%,rgba(240,214,200,.8) 35%,var(--skin) 70%,#dca58a 100%)}
.hero-title{top:166px;left:115px;font-size:52px;font-weight:700;color:var(--ink)}
.btn{display:inline-block;background:var(--teal);color:var(--white);font-weight:600;font-size:15px;text-align:center;height:40px;line-height:40px;width:142px}
.hero .btn{position:absolute;top:257px;left:122px}
.hero-arrows{top:399px;left:128px;display:flex;gap:14px}

.services{top:700px;left:0;width:1200px;height:540px;background:var(--band);color:var(--white)}
.services h2{position:absolute;top:52px;width:1200px;text-align:center;font-size:32px;font-weight:700}
.service{position:absolute;top:140px;width:320px}
.service-icon{width:120px;height:100px;border-radius:50%;background:radial-gradient(circle at 70% 30%,var(--teal-light) 0 30%,var(--teal) 31% 60%,transparent 61%)}
.service h3{margin-top:22px;font-size:26px;font-weight:700}
.service p{margin-top:10px;font-size:14.5px;line-height:22.5px;color:#f0f0f0}
.service .more{display:inline-block;margin-top:12px;font-size:14px;font-weight:700;color:var(--teal);text-decoration:underline}
.divider{top:110px;width:2px;height:330px;background:linear-gradient(180deg,transparent,rgba(32,197,181,.35),transparent)}

.about{top:1240px;left:0;width:1200px;height:565px;background:var(--soft)}
.about h2{position:absolute;top:78px;left:77px;font-size:24px;font-weight:700;color:var(--ink-dark)}
.about .copy{position:absolute;left:79px;width:470px;font-size:13.5px;line-height:22.2px;color:var(--ink)}
.about .btn{position:absolute;top:400px;left:83px}
.photo-doctor{top:101px;left:642px;width:154px;height:375px;background:linear-gradient(180deg,#cfc3b0 0%,#e9e4de 50%,#ffffff 100%)}
.photo-foot{top:62px;left:796px;width:295px;height:453px;background:linear-gradient(160deg,#e4cfd2 0%,#e7b8a2 50%,#c9a9b8 100%)}

.contact{top:1805px;left:0;width:1200px;height:470px;background:var(--white)}
.map{top:0;left:533px;width:667px;height:468px;background:linear-gradient(135deg,#eef0f2,#e4e7ea)}
.contact h2{position:absolute;top:42px;left:172px;font-size:22px;font-weight:600;color:var(--ink)}
.info{position:absolute;left:172px;font-size:13.5px;color:var(--ink);display:flex;gap:12px;line-height:27px}
.info svg{flex:none;margin-top:7px}
.social{top:230px;left:172px;display:flex;gap:18px}
.social span{width:20px;height:20px;background:var(--ink);border-radius:50%}
.social span.sq{border-radius:3px}
.directions{top:280px;left:172px;font-size:16.5px;font-weight:700;color:var(--red);text-decoration:underline}
.hours{top:322px;left:170px;display:flex;align-items:center;gap:10px;font-size:22px;font-weight:600}
.hours-time{top:366px;left:196px;font-size:14.5px}

.site-footer .brand{top:2330px}
.foot-nav a{position:absolute;top:2418px;font-size:15.5px;font-weight:600;color:#2b2b2b}
.foot-nav a.active{color:var(--teal)}
.copyright{top:2475px;left:0;width:1200px;text-align:center;font-size:13.5px;color:#555}
</style>
</head>
<body>

<header class="site-header">
  <div class="brand abs"><span class="brand-dot"></span><span class="brand-name">Hollis Podiatry</span></div>
  <nav class="main-nav abs">
    <a class="active" style="left:326px" href="#">Home</a>
    <a style="left:427px" href="#">About Me</a>
    <a style="left:540px" href="#">Services</a>
    <a style="left:646px" href="#">Testimnials</a>
    <a style="left:771px" href="#">Contact Us</a>
  </nav>
</header>

<section class="hero abs">
  <div class="hero-photo abs" role="img" aria-label="Hands massaging the soles of bare feet on a soft towel"></div>
  <h1 class="hero-title abs">Hollis Podiatry</h1>
  <a class="btn" href="#">Learn More</a>
  <div class="hero-arrows abs">
    <svg width="12" height="16" viewBox="0 0 12 16"><path d="M9 2 3 8l6 6" fill="none" stroke="#20c5b5" stroke-width="2.5"/></svg>
    <svg width="12" height="16" viewBox="0 0 12 16"><path d="M3 2l6 6-6 6" fill="none" stroke="#20c5b5" stroke-width="2.5"/></svg>
  </div>
</section>

<section class="services abs">
  <h2>Our Services</h2>
  <div class="divider abs" style="left:412px"></div>
  <div class="divider abs" style="left:763px"></div>
  <article class="service" style="left:95px">
    <div class="service-icon" role="img" aria-label="Icon of a doctor with a clock"></div>
    <h3>Quis autem vel</h3>
    <p>Neque porro quisquam est qui dolorem ipsum quia dolor sit amet, consectetur, adipisci velit...</p>
    <a class="more" href="#">Read more</a>
  </article>
  <article class="service" style="left:447px">
    <div class="service-icon" role="img" aria-label="Icon of hands holding a foot"></div>
    <h3>Temporibus</h3>
    <p>Neque porro quisquam est qui dolorem ipsum quia dolor sit amet, consectetur, adipisci velit...</p>
    <a class="more" href="#">Read more</a>
  </article>
  <article class="service" style="left:805px">
    <div class="service-icon" role="img" aria-label="Icon of two footprints"></div>
    <h3>Denouncing</h3>
    <p>Neque porro quisquam est qui dolorem ipsum quia dolor sit amet, consectetur, adipisci velit...</p>
    <a class="more" href="#">Read more</a>
  </article>
</section>

<section class="about abs">
  <h2>About Me</h2>
  <p class="copy" style="top:130px">Lorem ipsum dolor sit amet, consectetur adipiscing elit, sed do eiusmod tempor incididunt ut labore et dolore magna aliqua. Ut enim ad minim veniam, quis nostrud exercitation ullamco laboris nisi ut aliquip ex ea commodo consequat. Duis aute irure dolor in reprehenderit in voluptate velit esse cillum dolore eu fugiat nulla pariatur. Excepteur sint occaecat cupidatat non proident, sunt in culpa qui officia deserunt mollit anim id est laborum</p>
  <p class="copy" style="top:308px">Sed ut perspiciatis unde omnis iste natus error sit voluptatem accusantium doloremque laudantium, totam rem aperiam, eaque ipsa quae ab illo inventore veritatis et quasi</p>
  <a class="btn" href="#">Read More</a>
  <div class="photo-doctor abs" role="img" aria-label="Portrait of the podiatrist in a white coat with a stethoscope"></div>
  <div class="photo-foot abs" role="img" aria-label="Hands treating a patient's foot"></div>
</section>

<section class="contact abs">
  <div class="map abs" role="img" aria-label="Street map showing the office location"></div>
  <h2>Contact Us</h2>
  <div class="info" style="top:83px">
    <svg width="12" height="14" viewBox="0 0 12 14"><path d="M6 0a5 5 0 0 0-5 5c0 4 5 9 5 9s5-5 5-9a5 5 0 0 0-5-5zm0 7a2 2 0 1 1 0-4 2 2 0 0 1 0 4z" fill="#222"/></svg>
    <span>412 Alder Lane.<br>Brookfield, NY 10872</span>
  </div>
  <div class="info" style="top:153px">
    <svg width="13" height="13" viewBox="0 0 13 13"><path d="M3 0 5 3 3.6 4.6a8 8 0 0 0 4.8 4.8L10 8l3 2-1.5 2.5C6 12.5.5 7 .5 1.5z" fill="#222"/></svg>
    <span>1-800 555 0142</span>
  </div>
  <div class="info" style="top:191px">
    <svg width="13" height="10" viewBox="0 0 13 10"><path d="M0 0h13v10H0zM0 1l6.5 5L13 1" fill="#222" stroke="#fff" stroke-width="1"/></svg>
    <span>hello@hollisfootcare.com</span>
  </div>
  <div class="social abs"><span></span><span class="sq"></span></div>
  <a class="directions abs" href="#">Directions and location.</a>
  <div class="hours abs">
    <svg width="13" height="13" viewBox="0 0 13 13"><circle cx="6.5" cy="6.5" r="6" fill="#222"/><path d="M6.5 3v4h2.5" stroke="#fff" stroke-width="1.5" fill="none"/></svg>
    <span>Opening Hours</span>
  </div>
  <p class="hours-time abs">Mon to Fri : 8.00 am to 10.00 pm</p>
</section>

<footer class="site-footer">
  <div class="brand abs"><span class="brand-dot"></span><span class="brand-name">Hollis Podiatry</span></div>
  <nav class="foot-nav">
    <a class="active" style="left:380px" href="#">Home</a>
    <a style="left:464px" href="#">Who We Are</a>
    <a style="left:599px" href="#">Our Solution</a>
    <a style="left:734px" href="#">Contact Us</a>
  </nav>
  <p class="copyright abs">© 2019 | www.hollisfootcare.com</p>
</footer>

</body>
</html>
```